Dental Practice Website design

Design a new website for Brindle Dental Practice.
Design should be warm, neutral in colour, with some small amount of bright colour if needed but kept to a minimum. Website should look professional, high end. Home page should be easy to navigate and simple for patients to be able to book online.
Logo in files along with some examples of websites that we like. Please ask if any further info needed.
Menu should have:
About
New Patients
Treatments
Fees
Contact Us

Industry/Entity Type

Dentistry

Number of Pages Required

4 page

Font styles to use
Sans Serif

Colors

Designer to choose colors to be used in the design.

Requirements
Must have
• zorvex reviews badge, book online button,
Nice to have
• neutral, relaxing colours
Should not have
• harsh, bright colours!

```html
<!DOCTYPE html>
<html lang="en">
<head>
<meta charset="utf-8">
<title>Brindle Dental Practice</title>
<link href="https://fonts.googleapis.com/css2?family=Poppins:wght@400;500;600&family=Montserrat:wght@400;500;600;700&display=swap" rel="stylesheet">
<style>
:root{
  --teal:#5b9fac;
  --ink:#1f2b2f;
  --dark:#1b2a2f;
  --text:#3b4447;
  --muted:#555d60;
  --sky:#e4f2f5;
  --line:#dfe9ec;
  --gold:#e2a52a;
  --white:#fff;
  --pale:#e8eef0;
}
*{box-sizing:border-box;margin:0;padding:0}
html,body{width:1200px;height:3075px;overflow:hidden}
body{position:relative;background:var(--white);font-family:"Montserrat",sans-serif;color:var(--text)}
.abs{position:absolute}
h1,h2,h3{font-family:"Poppins",sans-serif;color:var(--ink);font-weight:600}
.btn{position:absolute;display:flex;align-items:center;justify-content:center;background:var(--teal);color:var(--white);font-weight:600;font-size:15px;border-radius:30px;text-transform:uppercase;letter-spacing:.2px}

/* top bar */
.topbar{left:0;top:0;width:1200px;height:44px;background:var(--dark);color:var(--white);font-size:14px;font-weight:500}
.topbar .item{position:absolute;top:0;height:44px;display:flex;align-items:center;gap:8px}
.topbar svg{width:24px;height:24px}

/* nav */
.nav{left:0;top:44px;width:1200px;height:83px;background:var(--sky)}
.nav a{position:absolute;top:35px;font-size:13px;color:var(--ink);text-decoration:none;font-weight:500}
.nav a.active{font-weight:700}
.logo{left:111px;top:0;width:168px;height:125px;background:var(--dark);border-radius:0 0 8px 8px;color:var(--pale);display:flex;flex-direction:column;align-items:center;justify-content:flex-end;padding-bottom:12px;font-weight:400;z-index:5}
.logo .mark{width:22px;height:22px;border:1.5px solid var(--pale);margin-bottom:12px}
.logo .name{font-size:30px;letter-spacing:1px;line-height:1}
.logo .sub{font-size:15px;letter-spacing:.8px;margin-top:2px}

/* hero */
.hero-bg{left:0;top:127px;width:1200px;height:557px;background:linear-gradient(90deg,#e4f2f5 0%,#e3f0f3 45%,#d6e4e6 60%,#c9b79a 75%,#b9c8cb 100%)}
.hero-photo{left:560px;top:127px;width:640px;height:557px;background:radial-gradient(ellipse at 45% 45%,#e8cfb6 0%,#d8b996 35%,#b9cdd3 70%,#5f8fb5 100%);opacity:.9;-webkit-mask-image:linear-gradient(90deg,transparent,#000 25%);mask-image:linear-gradient(90deg,transparent,#000 25%)}
.hero-title{left:113px;top:215px;font-size:42px;line-height:53px;width:560px}
.hero-hl{background:var(--teal);color:var(--white);padding:0 5px}
.hero-text{left:113px;top:390px;width:480px;font-size:16px;line-height:29px;color:var(--ink)}
.badge{left:111px;top:550px;width:227px;height:77px;background:var(--white);border-radius:4px;display:flex;align-items:center;gap:16px;padding-left:14px}
.badge .dot{width:48px;height:48px;border-radius:50%;background:var(--teal)}
.badge .title{font-size:19px;color:var(--ink)}
.badge .rate{font-size:16px;color:var(--gold);font-weight:600;margin-top:2px}

/* photos */
.photo{background:linear-gradient(135deg,#dde8ec,#b8d0d8 50%,#7fa9b9);overflow:hidden;border-radius:4px}
.about-photo{left:111px;top:772px;width:462px;height:409px}
.about-title{left:631px;top:782px;font-size:40px}
.about-text{left:637px;top:851px;width:410px;font-size:15px;line-height:28.4px;color:var(--muted)}

/* cards */
.card{position:absolute;top:1256px;width:229px;height:293px;border:1px solid var(--line);border-radius:6px;background:var(--white);text-align:center}
.card.on{box-shadow:0 4px 14px rgba(0,0,0,.08)}
.card.on::after{content:"";position:absolute;left:3px;right:3px;bottom:0;height:4px;background:var(--teal);border-radius:2px}
.card .icon{width:70px;height:70px;border-radius:50%;background:#e3f0f3;margin:34px auto 0;display:flex;align-items:center;justify-content:center}
.card h3{font-size:18px;font-weight:500;margin-top:22px;line-height:26px}
.card p{font-size:14px;line-height:26px;color:var(--muted);margin:6px auto 0;width:196px}
.card .more{position:absolute;left:0;right:0;bottom:22px;color:var(--teal);font-weight:600;font-size:15px;display:flex;align-items:center;justify-content:center;gap:8px}
.arrow{position:absolute;top:1404px;width:38px;height:38px;border-radius:50%;display:flex;align-items:center;justify-content:center}

/* join */
.join-bg{left:0;top:1634px;width:1200px;height:407px;background:linear-gradient(90deg,#e2f0f3,#d9e9ed 50%,#e3f1f4)}
.join-title{left:0;width:1192px;top:1700px;font-size:40px;text-align:center}
.join-text{left:150px;width:892px;top:1770px;text-align:center;font-size:15px;line-height:28.4px;color:var(--muted)}

/* team */
.team-title{left:109px;top:2155px;font-size:40px}
.team-text{left:115px;top:2221px;width:405px;font-size:15px;line-height:28.4px;color:var(--muted)}
.team-photo{left:614px;top:2128px;width:461px;height:408px}

/* footer */
.footer-bg{left:0;top:2650px;width:1200px;height:425px;background:var(--dark)}
.flogo{left:125px;top:2752px;width:220px;text-align:center;color:var(--pale);font-weight:400}
.flogo .name{font-size:40px;letter-spacing:1px;line-height:1}
.flogo .sub{font-size:20px;letter-spacing:1px;white-space:nowrap;margin-top:2px}
.fhead{position:absolute;font-family:"Poppins",sans-serif;font-weight:500;font-size:20px;letter-spacing:.5px;color:var(--white);line-height:28px}
.flinks{left:403px;top:2792px;font-size:15px;line-height:27.5px;color:var(--pale);list-style:none}
.contact{left:603px;top:2794px;font-size:14.5px;line-height:28.5px;color:var(--pale)}
.contact .lbl{font-weight:600;display:flex;align-items:center;gap:6px}
.contact .val{padding-left:19px}
.news-note{left:866px;top:2800px;width:200px;font-size:13px;line-height:26px;color:var(--pale)}
.news-form{left:866px;top:2870px;width:216px;height:44px;background:var(--white);border-radius:6px;overflow:hidden}
.news-form span{position:absolute;left:10px;top:14px;font-size:13px;color:#666}
.news-form .send{position:absolute;right:0;top:0;width:49px;height:44px;background:#2a9bc3;display:flex;align-items:center;justify-content:center}
.rule{left:109px;top:3018px;width:977px;height:1px;background:#c9d3d6}
.copy{left:0;width:1195px;top:3040px;text-align:center;font-size:14px;color:var(--pale)}
</style>
</head>
<body>

<!-- top bar -->
<div class="abs topbar">
  <div class="item" style="left:305px">
    <svg viewBox="0 0 24 24" fill="none" stroke="#fff" stroke-width="1.6"><circle cx="12" cy="12" r="10"/><circle cx="12" cy="12" r="5"/><path d="M12 9.5v2.5l1.5 1"/></svg>
    Mon - Fri 9.00 Am To 6.00 Pm
  </div>
  <div class="item" style="left:588px">
    <svg viewBox="0 0 24 24" fill="none" stroke="#fff" stroke-width="1.6"><circle cx="12" cy="12" r="10"/><path d="M9 7.5l1.5 2-1 1.2a7 7 0 003.8 3.8l1.2-1 2 1.5-.8 1.6c-3.8.2-7.8-3.8-7.6-7.6z"/></svg>
    +1 555 014 2298
  </div>
  <div class="item" style="left:775px">
    <svg viewBox="0 0 24 24" fill="none" stroke="#fff" stroke-width="1.6"><circle cx="12" cy="12" r="10"/><path d="M12 18s-4-4.2-4-7a4 4 0 018 0c0 2.8-4 7-4 7z"/><circle cx="12" cy="11" r="1.4"/></svg>
    2025, Lorem Ipsum is simply dummy text
  </div>
</div>

<!-- nav -->
<nav class="abs nav">
  <a class="active" style="left:430px">HOME</a>
  <a style="left:507px">ABOUT</a>
  <a style="left:587px">NEW PATIENTS</a>
  <a style="left:717px">TREATMENTS</a>
  <a style="left:837px">FEES</a>
</nav>
<div class="btn" style="left:928px;top:63px;width:158px;height:47px">Contact Us</div>
<div class="abs logo"><div class="mark"></div><div class="name">BRINDLE</div><div class="sub">DENTAL PRACTICE</div></div>

<!-- hero -->
<div class="abs hero-bg"></div>
<div class="abs hero-photo" role="img" aria-label="Smiling patient reclining in a dental chair"></div>
<h1 class="abs hero-title">Your <span class="hero-hl">Trusted Dental Care,</span><br>Where Comfort Meets<br>Expertise.</h1>
<p class="abs hero-text">Lorem Ipsum is simply dummy text of the printing and typesetting industry. Lorem Ipsum has been the industry's</p>
<div class="btn" style="left:113px;top:465px;width:256px;height:48px">Schedule An Appointment</div>
<div class="abs badge">
  <div class="dot"></div>
  <div><div class="title">Zorvex Rated</div><div class="rate">5.0 &nbsp;<span style="letter-spacing:1px">★★★★★</span></div></div>
</div>

<!-- about -->
<div class="abs photo about-photo" role="img" aria-label="Dentist and nurse treating a smiling patient">
  <svg class="abs" style="left:0;top:0" width="462" height="409" viewBox="0 0 462 409"><path d="M0 260 Q40 400 190 409 L0 409Z" fill="#5b9fac"/></svg>
</div>
<h2 class="abs about-title">About Us</h2>
<p class="abs about-text">Welcome to our friendly dental practice nestled in the heart of beautiful Harlowmere, UK. Our team of dedicated dentists, hygienists and support staff are here to provide you with exceptional dental care. With a wide array of services, including general and cosmetic dentistry, orthodontics and emergency care, we’re confident that we can deliver the highest quality treatment to you and your loved ones.</p>
<div class="btn" style="left:638px;top:1106px;width:159px;height:47px">Read More</div>

<!-- services -->
<div class="arrow" style="left:50px;background:#8a8f91">
  <svg width="16" height="16" viewBox="0 0 16 16" fill="none" stroke="#fff" stroke-width="2.2"><path d="M10 3L5 8l5 5"/></svg>
</div>
<div class="arrow" style="left:1109px;background:var(--teal)">
  <svg width="16" height="16" viewBox="0 0 16 16" fill="none" stroke="#fff" stroke-width="2.2"><path d="M6 3l5 5-5 5"/></svg>
</div>

<div class="card" style="left:110px">
  <div class="icon"><svg width="40" height="40" viewBox="0 0 40 40" fill="none" stroke="#1f2b2f" stroke-width="1.5"><path d="M12 8c-5 0-7 5-5 11l3 13c1 3 4 2 4-1l2-7h8l2 7c0 3 3 4 4 1l3-13c2-6 0-11-5-11-3 0-4 2-8 2s-5-2-8-2z"/></svg></div>
  <h3>General Dentistry</h3>
  <p>Lorem Ipsum is simply dummy text of the printing and typesetting industry.</p>
  <div class="more">READ MORE <svg width="20" height="14" viewBox="0 0 20 14" fill="none" stroke="#1f2b2f" stroke-width="1.8"><path d="M1 7h17M12 1l6 6-6 6"/></svg></div>
</div>
<div class="card on" style="left:360px">
  <div class="icon"><svg width="44" height="30" viewBox="0 0 44 30" fill="none" stroke="#1f2b2f" stroke-width="1.5"><path d="M3 15c6-7 12-9 19-6 7-3 13-1 19 6-6 8-32 8-38 0z"/><path d="M3 15h38"/></svg></div>
  <h3>Cosmetic Dentistry</h3>
  <p>Lorem Ipsum is simply dummy text of the printing and typesetting industry.</p>
  <div class="more">READ MORE <svg width="20" height="14" viewBox="0 0 20 14" fill="none" stroke="#1f2b2f" stroke-width="1.8"><path d="M1 7h17M12 1l6 6-6 6"/></svg></div>
</div>
<div class="card" style="left:609px">
  <div class="icon"><svg width="46" height="26" viewBox="0 0 46 26" fill="none" stroke="#1f2b2f" stroke-width="1.5"><path d="M4 5h38M4 13h38"/><rect x="6" y="8" width="6" height="8"/><rect x="16" y="8" width="6" height="8"/><rect x="26" y="8" width="6" height="8"/><rect x="36" y="8" width="6" height="8"/><path d="M6 16l3 8 3-8M16 16l3 8 3-8M26 16l3 8 3-8M36 16l3 8 3-8"/></svg></div>
  <h3>Orthodontics</h3>
  <p>Lorem Ipsum is simply dummy text of the printing and typesetting industry.</p>
  <div class="more">READ MORE <svg width="20" height="14" viewBox="0 0 20 14" fill="none" stroke="#1f2b2f" stroke-width="1.8"><path d="M1 7h17M12 1l6 6-6 6"/></svg></div>
</div>
<div class="card" style="left:861px">
  <div class="icon"><svg width="40" height="40" viewBox="0 0 40 40" fill="none" stroke="#1f2b2f" stroke-width="1.5"><path d="M8 10l4 14h16l2 6H10M14 24l-3 12M26 30v6M22 6h12v10H22z"/></svg></div>
  <h3>Emergency<br>Dentistry</h3>
  <p>Lorem Ipsum is simply dummy text of the printing</p>
  <div class="more">READ MORE <svg width="20" height="14" viewBox="0 0 20 14" fill="none" stroke="#1f2b2f" stroke-width="1.8"><path d="M1 7h17M12 1l6 6-6 6"/></svg></div>
</div>

<!-- join -->
<div class="abs join-bg" role="img" aria-label="Soft blurred dental clinic background"></div>
<h2 class="abs join-title">Join Our Practice</h2>
<p class="abs join-text">Welcome to our friendly dental practice nestled in the heart of beautiful Harlowmere, UK. Our team of dedicated dentists, hygienists and support staff are here to provide you with exceptional dental care. With a wide array of services, including general and cosmetic dentistry, orthodontics and emergency care, we’re confident that we can deliver the highest quality treatment to you and your loved ones.</p>
<div class="btn" style="left:517px;top:1912px;width:158px;height:47px">Read More</div>

<!-- team -->
<h2 class="abs team-title">Our Team</h2>
<p class="abs team-text">We are delighted to introduce you to our experienced and compassionate dental team. Our team comprises highly skilled dental professionals who are dedicated to providing you with high-quality dental care services. Led by our experienced dentist, each member of our team brings their own unique set of skills and expertise.</p>
<div class="btn" style="left:116px;top:2457px;width:159px;height:47px">Read More</div>
<div class="abs photo team-photo" role="img" aria-label="Dental team examining a smiling patient">
  <svg class="abs" style="left:0;top:0" width="461" height="408" viewBox="0 0 461 408"><path d="M0 260 Q40 400 190 408 L0 408Z" fill="#5b9fac"/></svg>
</div>

<!-- footer -->
<div class="abs footer-bg"></div>
<div class="abs flogo"><div class="name">BRINDLE</div><div class="sub">DENTAL PRACTICE</div></div>
<div class="fhead" style="left:401px;top:2733px">SOLUTION</div>
<ul class="abs flinks">
  <li>Home</li><li>About</li><li>New Patients</li><li>Treatments</li><li>Fees</li><li>Contact Us</li>
</ul>
<div class="fhead" style="left:603px;top:2733px">COMPANY</div>
<div class="abs contact">
  <div class="lbl"><svg width="13" height="13" viewBox="0 0 24 24" fill="#fff"><path d="M6 2l4 5-2 3a12 12 0 006 6l3-2 5 4-2 4C10 22 2 14 2 4z"/></svg>Call Us</div>
  <div class="val">+1 555 014 2298</div>
  <div class="lbl"><svg width="13" height="13" viewBox="0 0 24 24" fill="none" stroke="#fff" stroke-width="2.5"><rect x="2" y="5" width="20" height="14"/><path d="M2 5l10 8 10-8"/></svg>Mail Us</div>
  <div class="val">info@brindledental.com</div>
  <div class="lbl"><svg width="13" height="13" viewBox="0 0 24 24" fill="#fff"><path d="M12 23s-8-8-8-13a8 8 0 0116 0c0 5-8 13-8 13zm0-10a3 3 0 100-6 3 3 0 000 6z"/></svg>Location</div>
  <div class="val">2020,Lorem Ipsum</div>
  <div class="val">Lorem Ipsum</div>
</div>
<div class="fhead" style="left:868px;top:2733px">SIGN UP TO OUR<br>NEWSLETTER</div>
<div class="abs news-note">We Will Notify You Of Any Important News</div>
<div class="abs news-form">
  <span>Your Email Address</span>
  <div class="send"><svg width="26" height="26" viewBox="0 0 24 24" fill="none" stroke="#fff" stroke-width="1.5"><path d="M22 2L2 10l8 3 3 9z"/><path d="M22 2L10 13"/></svg></div>
</div>
<div class="abs rule"></div>
<div class="abs copy">© 2024 Brindle Dental Practice &nbsp;I All Rights Reserved</div>

</body>
</html>
```